Flyer-Design für Einzel- und Großhandel für Tuningteile
Zielgruppe
Die HLV GmbH ist im Einzel- und Großhandel für Tuningteile seit 9 Jahren tätig. Schwerpunktmäßig beschäftigen wir uns mit AERO Carbon Anbauteilen aus Carbon, Ansaugsystemen, Tuningboxen, Ladeluftkühlern, Bremsen und Kupplungen. Wir betrieben 7 Onlineshops die nach Themen oder Ländern gegliedert sind.
Gesucht wird ein Paketbeileger, der ausschließlich in unsere eigenen Pakete beigelegt wird. Zielgruppe sind also Bestandskunden - Alter, Einkommen ist stark gemischt. Unsere Zielgruppe ist zu 95+% männlich.
Aufgabenstellung
Der Paketbeileger soll 3 Zwecke erfüllen:
1. Ein persönliches Danke für deine Bestellung von der Geschäftsführung/dem Team von HLV.
2. Eine Bitte, uns auf Sicher Kaufen, Plauderbuch oder Findolo zu bewerten (Versionen mit 5% Incentive und ohne)
3. Ein Hinweis darauf, dass wir 5 unterschiedliche Onlineshops haben:
- www.hl-vortex.de : Hochwertige Carbon Autoteile und Norvalo Ansaugsysteme
- www.tq7-laden.de: TQ7 von Winkel Rennwerk. Die besten Tuningboxen aus den USA!
- www.pmlkuehl.de: Hochleistungs Ladeluftkühler zu günstigen Preisen.
- www.stark-kiste.de: Hochfeste Pellham Motorsport-Kupplungen.
- www.haltekeil.de: Die besten Bremsen zu besten Preisen.
- www.dröhnrohr.de: Die besten Sportauspuffanlagen. Gönn dir laut!
(Das Wording kann gerne anders sein!)
Ansprüche an das Design:
- Der Flyer muss sehr hochwertig wirken und wird später auf entsprechendem Material gedruckt.
- Der Look muss exklusiv und qualitativ hochwertig sein.
- Maße sind frei wählbar. Das Design steht hier im Vordergrund. Alles was gut und exklusiv aussieht geht.
- Optimal wäre es, wenn die 3 Geschäftsführer mit Bild und eventuell Zitat im Flyer zu sehen sind.
Die Ziele des Flyers sind:
1. Zum WOW-Effekt beim Auspacken beizutragen
2. Bewertungen zu generieren
3. Cross-Sales in den anderen Shops anzustoßen und den Kunden klarmachen, welche Bandbreite von Produkten bei uns erhältlich ist.

```html
<!DOCTYPE html>
<html lang="de">
<head>
<meta charset="utf-8">
<title>HLV Paketbeileger – Danke</title>
<link href="https://fonts.googleapis.com/css2?family=Raleway:wght@300;400;600;700;800&family=Allura&display=swap" rel="stylesheet">
<style>
  :root {
    --page-bg: #e9e9e9;
    --panel-light: #e6e4e1;
    --panel-dark: #414141;
    --shop-bg-top: #9a9a9a;
    --shop-bg-bottom: #7e7e7e;
    --ink: #3c3c3c;
    --ink-soft: #555555;
    --ink-light: #e8e8e8;
    --rule: #cfcfcf;
    --portrait: #8c8c8c;
  }
  * { box-sizing: border-box; margin: 0; padding: 0; }
  html, body { width: 1200px; height: 738px; overflow: hidden; }
  body {
    background: var(--page-bg);
    font-family: "Raleway", sans-serif;
    color: var(--ink);
    position: relative;
  }
  .flyer {
    position: absolute;
    left: 40px; top: 89px;
    width: 1120px; height: 560px;
    display: flex;
    box-shadow: 0 10px 30px rgba(0,0,0,0.12);
  }
  /* Left spread: thank-you */
  .thanks {
    width: 340px; height: 100%;
    background: var(--panel-light);
    padding: 50px 36px 0 30px;
    text-align: right;
    position: relative;
  }
  .thanks__title {
    font-weight: 700; font-size: 46px; letter-spacing: 1px; color: var(--ink-soft);
    line-height: 1;
  }
  .thanks__subtitle {
    font-weight: 300; font-size: 30px; color: var(--ink-soft); margin-top: 4px;
  }
  .thanks__body {
    margin-top: 40px; font-size: 14px; line-height: 1.36; color: var(--ink-soft);
    padding-left: 80px;
  }
  .thanks__review {
    margin-top: 16px; font-size: 13px; line-height: 1.36; color: var(--ink-soft);
    padding-left: 80px; font-weight: 600;
  }
  .thanks__signature {
    position: absolute; right: 36px; bottom: 26px;
    font-family: "Allura", cursive; font-size: 24px; line-height: 1; color: var(--ink-soft);
  }
  /* Management strip */
  .team {
    width: 220px; height: 100%;
    background: var(--panel-dark);
    display: flex; flex-direction: column; align-items: center;
    padding-top: 26px; gap: 22px;
  }
  .team__member { text-align: center; }
  .team__portrait {
    width: 130px; height: 130px;
    background: linear-gradient(160deg, #a8a8a8, var(--portrait) 60%, #5a5a5a);
    margin: 0 auto;
  }
  .team__name {
    color: var(--ink-light); font-size: 12px; letter-spacing: 1px; margin-top: 8px;
    text-transform: uppercase; font-weight: 400;
  }
  .team__name b { font-weight: 700; }
  /* Right spread: online shops */
  .shops {
    flex: 1; height: 100%; position: relative;
    padding: 40px 40px 0 40px;
    overflow: hidden;
  }
  .shops__photo {
    position: absolute; inset: 0;
    background: radial-gradient(ellipse at 55% 45%, #6f6f6f 0%, transparent 55%),
                linear-gradient(180deg, var(--shop-bg-top), var(--shop-bg-bottom));
  }
  .shops__content { position: relative; }
  .shops__title {
    font-weight: 800; font-size: 40px; letter-spacing: 1px; color: #353535; line-height: 1;
  }
  .shops__lead { font-size: 17px; color: #454545; margin-top: 2px; }
  .shops__list { list-style: none; margin-top: 26px; }
  .shops__item { margin-bottom: 18px; }
  .shops__url { font-weight: 700; font-size: 23px; color: #333; line-height: 1.1; }
  .shops__desc { font-size: 13px; color: #444; }
  .shops__footer {
    position: absolute; left: 20px; right: 20px; bottom: 28px; text-align: center;
  }
  .shops__rule { width: 220px; height: 1px; background: var(--rule); margin: 0 auto 10px; }
  .shops__claim {
    font-size: 11px; letter-spacing: 1.5px; color: var(--ink-light);
    text-transform: uppercase; white-space: nowrap;
  }
</style>
</head>
<body>
  <main class="flyer">
    <section class="thanks">
      <h1 class="thanks__title">DANKE</h1>
      <p class="thanks__subtitle">ipsum dolor sit</p>
      <p class="thanks__body">Lorem ipsum dolor sit amet, consectetur adipiscing elit, sed do eiusmod tempor incididunt ut labore et dolore magna aliqua. Ut enim ad minim veniam, quis nostrud exercitation ullamco laboris nisi ut aliquip ex ea commodo consequat. Duis aute irure dolor in reprehenderit in nulla.</p>
      <p class="thanks__review">Bewerte uns auf Sicher Kaufen, Plauderbuch oder Findolo!</p>
      <p class="thanks__signature">Ihre HLV Team</p>
    </section>

    <section class="team">
      <figure class="team__member">
        <div class="team__portrait" role="img" aria-label="Porträtfoto Geschäftsführer Jonas Wertheim"></div>
        <figcaption class="team__name">Jonas <b>Wertheim</b></figcaption>
      </figure>
      <figure class="team__member">
        <div class="team__portrait" role="img" aria-label="Porträtfoto Geschäftsführer Lukas Brandner"></div>
        <figcaption class="team__name">Lukas <b>Brandner</b></figcaption>
      </figure>
      <figure class="team__member">
        <div class="team__portrait" role="img" aria-label="Porträtfoto Geschäftsführer Tobias Kehrwald"></div>
        <figcaption class="team__name">Tobias <b>Kehrwald</b></figcaption>
      </figure>
    </section>

    <section class="shops">
      <div class="shops__photo" role="img" aria-label="Schwarzweißfoto eines getunten Sportwagens von hinten auf einer Allee"></div>
      <div class="shops__content">
        <h2 class="shops__title">ONLINESHOPS</h2>
        <p class="shops__lead">Wir bieten die größten auswahl an carbon teilen</p>
        <ul class="shops__list">
          <li class="shops__item"><p class="shops__url">www.hl-vortex.de</p><p class="shops__desc">Hochwertige Carbon Autoteile und Norvalo Ansaugsysteme</p></li>
          <li class="shops__item"><p class="shops__url">www.tq7-laden.de</p><p class="shops__desc">TQ7 von Winkel Rennwerk. Die besten Tuningboxen aus den USA!</p></li>
          <li class="shops__item"><p class="shops__url">www.pmlkuehl.de</p><p class="shops__desc">Hochleistungs Ladeluftkühler zu günstigen Preisen</p></li>
          <li class="shops__item"><p class="shops__url">www.stark-kiste.de</p><p class="shops__desc">Hochfeste Pellham Motorsport-Kupplungen</p></li>
          <li class="shops__item"><p class="shops__url">www.haltekeil.de</p><p class="shops__desc">Die besten Bremsen zu besten Preisen</p></li>
        </ul>
      </div>
      <footer class="shops__footer">
        <div class="shops__rule"></div>
        <p class="shops__claim">Heliovortex Leichtbau - Ein Element, endlose Möglichkeiten!</p>
      </footer>
    </section>
  </main>
</body>
</html>
```